TalkBridge - Language Coaching Services

Sleek, innovative, trendy design for Language Coaching business.

TalkBridge is a new UK based company that provides Language Coaching services. We offer highly personalized on-line and face to face language courses. We also impart learning techniques workshops based on the latest neuroscience research for second-language acquisition.

Target Market(s)

Industry/Entity Type

Consulting

Contact Information for Business Card

TalkBridge
ElenaVT@talkbridge-demo.co.uk
TalkBridge-demo.co.uk
London, UK

Font styles to use
Sans Serif

```html
<!DOCTYPE html>
<html lang="en">
<head>
<meta charset="utf-8">
<title>TalkBridge – Business Card</title>
<link rel="stylesheet" href="https://fonts.googleapis.com/css2?family=Montserrat:wght@400;500;600&family=Roboto+Condensed:ital,wght@0,400;1,400&display=swap">
<style>
  :root {
    --bg: #2b2d30;
    --card-light: #f4f5f6;
    --card-dark: #232425;
    --blue: #1a7cb8;
    --blue-bright: #1aa3e0;
    --blue-deep: #0d5f94;
    --ink: #3a3f45;
    --grey-text: #c9cbcd;
    --rule: #5a5d61;
  }
  * { margin: 0; padding: 0; box-sizing: border-box; }
  html, body { width: 1200px; height: 900px; overflow: hidden; }
  body {
    background: var(--bg);
    font-family: "Montserrat", sans-serif;
    position: relative;
  }
  .card {
    position: absolute;
    left: 280px;
    width: 640px;
    height: 366px;
    border-radius: 22px;
    overflow: hidden;
    box-shadow: 0 14px 30px rgba(0,0,0,.45);
  }
  /* Front */
  .card-front { top: 52px; background: linear-gradient(135deg, #ffffff 0%, var(--card-light) 60%, #e6e8ea 100%); }
  .front-wave { position: absolute; left: 0; bottom: 0; width: 640px; height: 366px; }
  .brand { position: absolute; left: 50px; top: 48px; display: flex; align-items: center; gap: 14px; }
  .brand-dot { width: 38px; height: 38px; border-radius: 50%; background: var(--blue); }
  .brand-name { font-size: 40px; font-weight: 500; color: var(--blue); letter-spacing: 1px; }
  .front-rule { position: absolute; left: 50px; right: 50px; top: 140px; height: 2px; background: var(--blue-deep); }
  .contact { position: absolute; left: 50px; top: 166px; list-style: none; font-size: 15px; color: var(--ink); line-height: 26px; }
  .contact li { display: flex; align-items: center; gap: 10px; }
  .contact svg { width: 12px; height: 12px; fill: var(--blue-deep); }
  .contact strong { font-weight: 600; color: var(--blue-deep); }
  .person { position: absolute; right: 50px; top: 160px; text-align: right; }
  .person-name { font-size: 28px; font-weight: 600; letter-spacing: 1px; color: var(--blue-deep); text-transform: uppercase; }
  .person-name span { color: var(--blue-bright); }
  .person-role { font-size: 15px; color: var(--ink); margin-top: 2px; letter-spacing: 1px; }
  .address { position: absolute; right: 50px; top: 250px; text-align: right; font-size: 15px; color: var(--ink); line-height: 24px; letter-spacing: .5px; }
  /* Back */
  .card-back { top: 482px; background: var(--card-dark); text-align: center; color: var(--grey-text); font-family: "Roboto Condensed", sans-serif; }
  .back-brand { margin-top: 40px; display: flex; justify-content: center; align-items: center; gap: 14px; }
  .back-brand .brand-name { font-family: "Montserrat", sans-serif; }
  .services-title { margin-top: 18px; font-size: 26px; color: var(--blue); }
  .tagline { margin-top: 12px; font-size: 19px; font-style: italic; color: var(--blue-bright); }
  .back-rule { width: 540px; height: 1px; background: var(--rule); margin: 14px auto 16px; }
  .services { font-size: 17px; line-height: 27px; }
  .services .sep { color: var(--blue-bright); padding: 0 4px; }
</style>
</head>
<body>
  <section class="card card-front">
    <svg class="front-wave" viewBox="0 0 640 366" aria-hidden="true">
      <path d="M0 250 C150 275 300 300 420 366 L0 366 Z" fill="var(--blue-deep)"/>
      <path d="M0 238 C160 262 320 290 430 366 L418 366 C310 298 150 272 0 250 Z" fill="var(--blue-bright)"/>
    </svg>
    <div class="brand"><span class="brand-dot"></span><span class="brand-name">TalkBridge</span></div>
    <div class="front-rule"></div>
    <ul class="contact">
      <li><svg viewBox="0 0 24 24"><path d="M6.6 10.8a15 15 0 0 0 6.6 6.6l2.2-2.2a1 1 0 0 1 1-.25 11.4 11.4 0 0 0 3.6.57 1 1 0 0 1 1 1V20a1 1 0 0 1-1 1A17 17 0 0 1 3 4a1 1 0 0 1 1-1h3.5a1 1 0 0 1 1 1c0 1.25.2 2.45.57 3.57a1 1 0 0 1-.25 1z"/></svg>(555) 010-4821</li>
      <li><svg viewBox="0 0 24 24"><path d="M2 5h20v14H2z M2 5l10 8 10-8" fill="none" stroke="var(--blue-deep)" stroke-width="2.5"/></svg>info@talkbridge-demo.co.uk</li>
      <li><svg viewBox="0 0 24 24"><circle cx="12" cy="12" r="10"/></svg>www.<strong>talkbridge-demo</strong>.co.uk</li>
    </ul>
    <div class="person">
      <div class="person-name">Daniel <span>Hart</span></div>
      <div class="person-role">Director</div>
    </div>
    <address class="address">18 Harbour Lane,<br>London, UK, EC1A 4PQ</address>
  </section>

  <section class="card card-back">
    <div class="back-brand"><span class="brand-dot"></span><span class="brand-name">TalkBridge</span></div>
    <h2 class="services-title">Our Services</h2>
    <p class="tagline">We offer highly customized coaching sessions and self-study content.</p>
    <div class="back-rule"></div>
    <p class="services">
      Face to face language coaching sessions<span class="sep">|</span>On-line language coaching sessions<br>
      Personalized Newsletters for self-learners<span class="sep">|</span>Language Learning Techniques Workshops<br>
      Mindful Learning Workshops<span class="sep">|</span>Access to premium content, resources.
    </p>
  </section>
</body>
</html>
```